Motor Vault Website - Part of the Brantley Group

A complimentary website is required for the launch of a 'Motor Vault' - a new service launched by industry renowned BRANTLEY. Motor Vault is an industry-first brand that designs and builds unique subterranean car parks for private residential homes in London and the influential counties within the UK. Please see here the direction of a new BRANTLEY Website - we would like Motor Vault to be complimentary and sit alongside BRANTLEY harmoniously - https://www.brantleyhq.example/brantley-nu-staging Brantley have some images, but whilst more professional images are in production - we have also attached pixmoor photos- named clearly as pixmoor. **Attached files include JPEG, .eps of logo and Brantley library images and Pixmoor Library Images - two versions of logo dependent on background colour. - Website needs to be sleek, chic and masculine.- Colour Palette - Grey/ Black/ White - Same visiual journey as Brantley website- Required areas within the sit include - About Us / Our Work / Contact Page

Target Market(s)

Luxury
Men

Number of Pages Required

2 page

Font styles to use
Sans Serif

Colors
e8e8e8
757575
1b1b1b
000000
9d9d9d
cbcbcb
f5f5f5

Requirements
Must have
• Complimentary of this site - https://www.brantleyhq.example/brantley-nu-staging
Should not have
• Colour

```html
<!DOCTYPE html>
<html lang="en">
<head>
<meta charset="utf-8">
<title>Motor Vault — Part of the Brantley Group</title>
<link rel="stylesheet" href="https://fonts.googleapis.com/css2?family=Roboto:wght@400;500;700&family=Montserrat:wght@500&display=swap">
<style>
  :root {
    --black: #000000;
    --ink: #1b1b1b;
    --strip: #0c0c0c;
    --grey-dark: #757575;
    --grey-mid: #9d9d9d;
    --grey-light: #cbcbcb;
    --mist: #e8e8e8;
    --paper: #f5f5f5;
    --white: #ffffff;
  }
  * { box-sizing: border-box; margin: 0; padding: 0; }
  html, body { width: 1200px; height: 1000px; overflow: hidden; }
  body {
    position: relative;
    background: var(--white);
    font-family: 'Roboto', Arial, sans-serif;
    color: var(--ink);
  }

  .hero {
    position: absolute; left: 0; top: 0; width: 1200px; height: 702px;
    background:
      radial-gradient(ellipse 420px 320px at 600px 390px, #3a3a3a 0%, rgba(40,40,40,0) 100%),
      linear-gradient(180deg, #1e1e1e 0%, #2a2a2a 35%, #262626 70%, #1c1c1c 100%);
  }
  .top-strip {
    position: absolute; left: 0; top: 0; width: 1200px; height: 8px;
    background: var(--strip);
  }

  .brand {
    position: absolute; left: 0; top: 14px; width: 1200px; text-align: center;
  }
  .brand-name {
    display: inline-flex; align-items: center; gap: 14px;
    font-family: 'Montserrat', Arial, sans-serif; font-weight: 500;
    font-size: 44px; line-height: 48px; letter-spacing: 1px;
    color: var(--mist);
  }
  .brand-mark {
    width: 32px; height: 32px; background: var(--mist);
  }
  .brand-tagline {
    position: absolute; left: 638px; top: 66px;
    font-family: 'Montserrat', Arial, sans-serif; font-weight: 500;
    font-size: 9.5px; letter-spacing: 0.2px; color: var(--grey-mid);
  }

  .main-nav {
    position: absolute; left: 136px; top: 89px; width: 926px; height: 66px;
    background: var(--white);
  }
  .main-nav a {
    position: absolute; top: 28px; font-size: 12.2px; line-height: 15px;
    color: var(--ink); text-decoration: none; letter-spacing: 0;
  }
  .main-nav a.is-current {
    top: 25px; left: 161px; padding: 2px 7px; border: 1.5px solid var(--ink);
    font-weight: 700;
  }
  .search-icon { position: absolute; left: 797px; top: 21px; }

  .slide-arrow { position: absolute; top: 340px; }
  .slide-arrow.prev { left: 38px; }
  .slide-arrow.next { left: 1143px; }

  .bracket { position: absolute; }
  .bracket.top-left { left: 330px; top: 306px; }
  .bracket.bottom-right { left: 823px; top: 483px; }

  .hero-title {
    position: absolute; left: 314px; top: 324px; width: 600px;
    text-align: center; font-weight: 700; font-size: 43px; line-height: 52px;
    color: var(--white); letter-spacing: 0.3px;
  }
  .hero-copy {
    position: absolute; left: 354px; top: 393px; width: 520px;
    text-align: center; font-size: 17.4px; line-height: 23.5px; color: var(--white);
  }

  .feature-photo { position: absolute; top: 641px; width: 383px; height: 359px; }
  .feature-photo.welding {
    left: 157px;
    background: linear-gradient(160deg, #2a2a2a 0%, #141414 45%, #4a4a4a 75%, #2c2c2c 100%);
  }
  .feature-photo.garage {
    left: 660px;
    background:
      radial-gradient(ellipse 120px 90px at 190px 170px, #bdbdbd 0%, rgba(150,150,150,0) 100%),
      linear-gradient(180deg, #1e1e1e 0%, #3a3a3a 45%, #8a8a8a 75%, #9a9a9a 100%);
  }
</style>
</head>
<body>
  <section class="hero" role="img" aria-label="Dark concrete underground car park lit from the ceiling"></section>
  <div class="top-strip"></div>

  <header class="brand">
    <span class="brand-name"><span class="brand-mark"></span>MOTOR VAULT</span>
  </header>
  <span class="brand-tagline">PART OF THE BRANTLEY GROUP</span>

  <nav class="main-nav">
    <a href="#" class="is-current">HOME</a>
    <a href="#" style="left:243px">STRUCTURAL</a>
    <a href="#" style="left:355px">INTERIORS</a>
    <a href="#" style="left:454px">ABOUT</a>
    <a href="#" style="left:532px">PORTFOLIO</a>
    <a href="#" style="left:632px">NEWS</a>
    <a href="#" style="left:702px">CONTACT</a>
    <svg class="search-icon" width="28" height="28" viewBox="0 0 28 28" aria-label="Search">
      <circle cx="11.5" cy="11.5" r="9.5" fill="none" stroke="#1b1b1b" stroke-width="1.8"/>
      <line x1="18.5" y1="18.5" x2="26" y2="26" stroke="#1b1b1b" stroke-width="1.8"/>
    </svg>
  </nav>

  <svg class="slide-arrow prev" width="20" height="34" viewBox="0 0 20 34" aria-label="Previous slide">
    <polyline points="17,1 2,17 17,33" fill="none" stroke="#9d9d9d" stroke-width="1.6"/>
  </svg>
  <svg class="slide-arrow next" width="20" height="34" viewBox="0 0 20 34" aria-label="Next slide">
    <polyline points="3,1 18,17 3,33" fill="none" stroke="#9d9d9d" stroke-width="1.6"/>
  </svg>

  <svg class="bracket top-left" width="47" height="47" viewBox="0 0 47 47">
    <polyline points="1.5,46 1.5,1.5 46,1.5" fill="none" stroke="#ffffff" stroke-width="3"/>
  </svg>
  <svg class="bracket bottom-right" width="47" height="46" viewBox="0 0 47 46">
    <polyline points="1,44 45,44 45,1" fill="none" stroke="#ffffff" stroke-width="3"/>
  </svg>

  <h1 class="hero-title">WE LEAD. WE INVENT</h1>
  <p class="hero-copy">Lorem ipsum dolor sit amet, consectetur adipiscing<br>elit, sed do eiusmod tempor incididunt ut labore et<br>dolore magna aliqua. Quis ipsum suspendisse ul-<br>trices gravida. Risus commodo viverra maecenas<br>accumsan lacus vel facilisis.</p>

  <div class="feature-photo welding" role="img" aria-label="Worker welding a steel beam with sparks flying"></div>
  <div class="feature-photo garage" role="img" aria-label="Empty concrete garage with steel columns leading to bright opening"></div>
</body>
</html>
```